Building Company Business Card Design

I am looking to get a business card designed for my Building Company. Please find the logo attached.

Industry/Entity Type

Business

Contact Information for Business Card

Mobile 0472 913 046
Email admin@tarrowconstructworks.com.au
Website www.tarrowconstructworks.com.au

Colors
0255a3

```html
<!DOCTYPE html>
<html lang="en">
<head>
<meta charset="utf-8">
<title>Tarrow Construct Works – Business Card</title>
<link rel="stylesheet" href="https://fonts.googleapis.com/css2?family=Questrial&display=swap">
<style>
  :root {
    --brand-blue: #0255a3;
    --band-grey: #6f7073;
    --card-top: #ffffff;
    --card-bottom: #e6e7e9;
    --ink-grey: #4f5054;
    --stage: #d9dadc;
  }
  * { margin: 0; padding: 0; box-sizing: border-box; }
  html, body { width: 1200px; height: 834px; overflow: hidden; }
  body {
    background: var(--stage);
    font-family: "Questrial", "Century Gothic", sans-serif;
    position: relative;
  }
  .card {
    position: absolute;
    width: 540px;
    height: 309px;
    background: linear-gradient(160deg, var(--card-top) 0%, var(--card-bottom) 100%);
    box-shadow: 0 6px 18px rgba(0,0,0,0.18);
    overflow: hidden;
  }
  .card--front { left: 70px; top: 80px; }
  .card--back { left: 590px; top: 445px; }
  .card__wave { position: absolute; inset: 0; width: 100%; height: 100%; }
  .wordmark {
    position: absolute;
    display: flex;
    align-items: center;
    gap: 10px;
    color: var(--brand-blue);
    font-size: 22px;
    letter-spacing: 1px;
    white-space: nowrap;
  }
  .wordmark__square {
    width: 14px; height: 14px;
    background: var(--brand-blue);
  }
  .card--front .wordmark { left: 50%; top: 92px; transform: translateX(-50%); }
  .card--back .wordmark { left: 50%; top: 46px; transform: translateX(-50%); }
  .holder {
    position: absolute;
    left: 0; right: 0; top: 96px;
    text-align: center;
    font-size: 15px;
    color: var(--ink-grey);
    font-weight: 700;
  }
  .holder__role { color: var(--brand-blue); font-weight: 400; }
  .contacts {
    position: absolute;
    left: 120px; top: 128px;
    list-style: none;
    font-size: 12px;
    line-height: 19px;
    color: var(--ink-grey);
  }
  .contacts__label {
    display: inline-block;
    width: 18px;
    color: var(--brand-blue);
    font-weight: 700;
  }
</style>
</head>
<body>

  <section class="card card--front" aria-label="Business card front">
    <svg class="card__wave" viewBox="0 0 540 309" preserveAspectRatio="none" aria-hidden="true">
      <path d="M0 246 C 180 250, 380 210, 540 92 L 540 100 C 380 222, 180 258, 0 254 Z" fill="var(--band-grey)"/>
      <path d="M0 258 C 180 262, 390 226, 540 108 L 540 309 L 0 309 Z" fill="var(--brand-blue)"/>
    </svg>
    <div class="wordmark"><span class="wordmark__square"></span>TARROW CONSTRUCT WORKS</div>
  </section>

  <section class="card card--back" aria-label="Business card back">
    <svg class="card__wave" viewBox="0 0 540 309" preserveAspectRatio="none" aria-hidden="true">
      <path d="M0 258 C 190 262, 400 230, 540 120 L 540 127 C 400 238, 190 268, 0 265 Z" fill="var(--band-grey)"/>
      <path d="M0 270 C 190 274, 405 242, 540 133 L 540 309 L 0 309 Z" fill="var(--brand-blue)"/>
    </svg>
    <div class="wordmark"><span class="wordmark__square"></span>TARROW CONSTRUCT WORKS</div>
    <p class="holder">Liam Carter <span class="holder__role">– President</span></p>
    <ul class="contacts">
      <li><span class="contacts__label">M</span>0472 913 046</li>
      <li><span class="contacts__label">E</span>admin@tarrowconstructworks.com.au</li>
      <li><span class="contacts__label">W</span>www.tarrowconstructworks.com.au</li>
    </ul>
  </section>

</body>
</html>
```